Ridgely Forge business card for handing simple contact information and generating service awareness

Utilizing the attached logo(s), generate a professional, but approachable, card conveying a sense of capability and integrity. Please only use one logo of the four attached; the different colors are all acceptable, but preference will be given to a design integrating a teal/turquoise logo,

I do not know where to put in the contact information or details?

Target Market(s)

Agriculture, Farming, Timber, Forestry, Construction, Crane Service

Industry/Entity Type

Contact Information for Business Card

Name, Phone Number, email address

Colors

Designer to choose colors to be used in the design.

Requirements
Nice to have
• It would be great to have either a mountain or one of the attached cranes as a backdrop on the rear of the card. Simple watermarks and/or Debossing is also great

```html
<!DOCTYPE html>
<html lang="en">
<head>
<meta charset="utf-8">
<title>Ridgely Forge – Business Card</title>
<link rel="stylesheet" href="https://fonts.googleapis.com/css2?family=Lato:wght@400;700;900&display=swap">
<style>
  :root {
    --teal: #276e61;
    --paper: #ffffff;
    --backdrop: #e6e8e7;
    --card-shadow: rgba(0, 0, 0, 0.18);
  }
  * { box-sizing: border-box; margin: 0; padding: 0; }
  html, body {
    width: 1200px;
    height: 982px;
    overflow: hidden;
    background: var(--backdrop);
    font-family: "Lato", sans-serif;
  }
  .canvas {
    position: relative;
    width: 1200px;
    height: 982px;
  }
  .card {
    position: absolute;
    width: 700px;
    height: 400px;
    border-radius: 26px;
    background: var(--paper);
    overflow: hidden;
    box-shadow: 0 10px 28px var(--card-shadow);
  }
  .card-front { left: 420px; top: 60px; }
  .card-back  { left: 80px;  top: 520px; }

  .brand {
    position: absolute;
    display: flex;
    align-items: center;
    gap: 14px;
    color: var(--teal);
    font-family: "Lato", sans-serif;
    font-weight: 900;
    text-transform: uppercase;
    letter-spacing: 1px;
    white-space: nowrap;
  }
  .brand-dot {
    width: 22px;
    height: 22px;
    border-radius: 50%;
    background: var(--teal);
    flex: none;
  }
  .card-front .brand {
    left: 0; right: 0; top: 0; bottom: 0;
    justify-content: center;
    font-size: 46px;
  }
  .card-back .brand {
    left: 380px;
    right: 20px;
    top: 0; bottom: 0;
    justify-content: center;
    font-size: 32px;
  }
  .card-back .brand-dot { width: 16px; height: 16px; }

  .back-panel {
    position: absolute;
    inset: 0;
    width: 700px;
    height: 400px;
  }
  .contact {
    position: absolute;
    left: 40px;
    top: 42px;
    color: var(--paper);
  }
  .contact-name {
    font-weight: 700;
    font-size: 31px;
    letter-spacing: 0.5px;
    text-transform: uppercase;
    line-height: 1.05;
  }
  .contact-title {
    font-size: 19px;
    margin-bottom: 16px;
  }
  .contact-list { list-style: none; }
  .contact-list li {
    display: flex;
    align-items: flex-start;
    gap: 10px;
    font-size: 17px;
    line-height: 1.45;
  }
  .contact-list svg {
    width: 14px;
    height: 14px;
    margin-top: 5px;
    flex: none;
    fill: var(--paper);
  }
</style>
</head>
<body>
<main class="canvas">

  <section class="card card-front" aria-label="Card front">
    <div class="brand"><span class="brand-dot"></span>Ridgely Forge</div>
  </section>

  <section class="card card-back" aria-label="Card back">
    <svg class="back-panel" viewBox="0 0 700 400" aria-hidden="true">
      <path fill="var(--teal)" d="M0,0 H350 C280,60 320,160 350,250 C375,330 290,385 230,400 H0 Z"/>
      <path fill="none" stroke="var(--paper)" stroke-width="4" d="M334,0 C264,60 304,160 334,250 C359,330 274,385 214,400"/>
    </svg>

    <div class="contact">
      <h1 class="contact-name">Owen Hartley</h1>
      <p class="contact-title">Founder &amp; CEO</p>
      <ul class="contact-list">
        <li>
          <svg viewBox="0 0 16 16"><path d="M8 0a5.5 5.5 0 0 0-5.5 5.5C2.5 9.6 8 16 8 16s5.5-6.4 5.5-10.5A5.5 5.5 0 0 0 8 0zm0 7.7a2.2 2.2 0 1 1 0-4.4 2.2 2.2 0 0 1 0 4.4z"/></svg>
          <span>4870 Alder Creek Road<br>Millbrook, VT 05201</span>
        </li>
        <li>
          <svg viewBox="0 0 16 16"><path d="M3.6 1 6 3.8 4.6 5.6a9 9 0 0 0 5.8 5.8L12.2 10l2.8 2.4-1.6 2.6C7.6 15.2.8 8.4 1 2.6z"/></svg>
          <span>(555) 314-2087</span>
        </li>
        <li>
          <svg viewBox="0 0 16 16"><path d="M4 0h8a1 1 0 0 1 1 1v14a1 1 0 0 1-1 1H4a1 1 0 0 1-1-1V1a1 1 0 0 1 1-1zm1 2v10h6V2zm3 11a1 1 0 1 0 0 2 1 1 0 0 0 0-2z"/></svg>
          <span>(555) 314-2088</span>
        </li>
        <li>
          <svg viewBox="0 0 16 16"><path d="M4 0h8v4H4zM1 5h14a1 1 0 0 1 1 1v6h-3v4H3v-4H0V6a1 1 0 0 1 1-1zm4 6v3h6v-3z"/></svg>
          <span>(555) 314-2089</span>
        </li>
        <li>
          <svg viewBox="0 0 16 16"><path d="M0 3h16v1.2L8 9 0 4.2zm0 2.6 8 4.8 8-4.8V13H0z"/></svg>
          <span>info@ridgelyforge.com</span>
        </li>
        <li>
          <svg viewBox="0 0 16 16"><path d="M8 0a8 8 0 1 0 0 16A8 8 0 0 0 8 0zm5.9 7h-2.5a12 12 0 0 0-1-4.7A6 6 0 0 1 13.9 7zM8 2c.8 1 1.3 2.9 1.4 5H6.6C6.7 4.9 7.2 3 8 2zM5.6 2.3a12 12 0 0 0-1 4.7H2.1a6 6 0 0 1 3.5-4.7zM2.1 9h2.5a12 12 0 0 0 1 4.7A6 6 0 0 1 2.1 9zM8 14c-.8-1-1.3-2.9-1.4-5h2.8C9.3 11.1 8.8 13 8 14zm2.4-.3a12 12 0 0 0 1-4.7h2.5a6 6 0 0 1-3.5 4.7z"/></svg>
          <span>ridgelyforge.com</span>
        </li>
      </ul>
    </div>

    <div class="brand"><span class="brand-dot"></span>Ridgely Forge</div>
  </section>

</main>
</body>
</html>
```